Redesign vek7.ch agency website for unique design with speed and conversion

We want to redesign our website vek7.ch. Our omnichannel marketing agency builds webshops and integrates them into existing systems like ERP/CRM and supports with online marketing campaigns like plimtor ads and social media. The target of the redesign is to get a great look and feel for customers to see directly what we do, (please design something for our three focus areas eCommerce, Online marketing and Integration)
and to improve the pages speed drastically for SEO. Please see our attachment.
Target Market(s)
B2B
Industry/Entity Type
eCommerce Agency
Coding
Coded - Design and coding required
Number of Pages Required
5+ page
Look and feel
Each slider illustrates characteristics of the customer's brand and the style your logo design should communicate.

```html
<!DOCTYPE html>
<html lang="en">
<head>
<meta charset="utf-8">
<title>vek7 – Online marketing agency in Zurich</title>
<link rel="stylesheet" href="https://fonts.googleapis.com/css2?family=Chakra+Petch:wght@500;600;700&family=Roboto:wght@400;500;700&display=swap">
<style>
:root{
  --green:#4fe05b;
  --green-text:#4cd856;
  --dark:#111;
  --ink:#222;
  --pale:#f2fdea;
  --lime:#b6ea55;
  --white:#fff;
  --photo-grey:#bfc2c0;
  --suit:#2c3a52;
}
*{margin:0;padding:0;box-sizing:border-box}
html,body{width:1200px;height:4027px;overflow:hidden}
body{position:relative;font-family:"Roboto",sans-serif;color:var(--ink);background:var(--white)}
.abs{position:absolute}
.head{font-family:"Chakra Petch",sans-serif;font-weight:700;color:var(--green-text);text-transform:uppercase}
.photo{background:linear-gradient(135deg,#d9dbd9,#a9acaa 60%,var(--suit))}

/* header */
.topbar{left:0;top:0;width:1200px;height:73px;background:var(--pale)}
.logo{font-family:"Chakra Petch",sans-serif;font-weight:700;letter-spacing:2px}
.topbar .logo{left:148px;top:14px;font-size:38px;color:var(--green-text)}
.nav{left:331px;top:29px;display:flex;gap:26px;font-size:11px;font-weight:700;color:var(--dark)}
.nav .active{color:var(--green-text)}

/* hero */
.hero{left:0;top:73px;width:1200px;height:519px;background:var(--green)}
.hero-title{left:148px;top:154px;font-family:"Chakra Petch",sans-serif;font-weight:600;font-size:42px;line-height:54px;color:var(--white)}
.hero-sub{left:148px;top:281px;font-size:17px;line-height:22px;color:var(--dark)}
.btn{border:2px solid var(--dark);border-radius:24px;font-weight:700;font-size:17px;display:flex;align-items:center;justify-content:center;color:var(--dark)}
.btn-offers{left:147px;top:364px;width:116px;height:50px}
.btn-deadline{left:273px;top:364px;width:141px;height:50px;border-color:var(--white);color:var(--dark)}
.portrait-top{left:870px;top:0;width:258px;height:356px;border-radius:0 0 110px 110px;border:3px solid var(--dark);padding:6px;background:var(--pale)}
.portrait-top div,.portrait-low div{width:100%;height:100%;border-radius:inherit}
.portrait-low{left:605px;top:230px;width:256px;height:362px;border-radius:110px 110px 0 0;border:3px solid var(--dark);border-bottom:none;padding:6px 6px 0;background:var(--pale)}

/* services */
.sec-title{width:1200px;left:0;text-align:center;font-size:41px}
.card{top:791px;width:281px;height:375px;background:var(--white);border-radius:0 0 0 60px;box-shadow:4px 6px 10px rgba(0,0,0,.2);text-align:center}
.card-img{width:100%;height:197px;border-radius:0 0 0 60px}
.card-icon{position:absolute;left:118px;top:165px;width:46px;height:46px;border-radius:50%;background:var(--white);border:2px solid var(--green);display:flex;align-items:center;justify-content:center}
.card h3{margin-top:29px;font-family:"Roboto",sans-serif;font-weight:500;font-size:17px;color:var(--green-text)}
.card p{margin:6px auto 0;width:240px;font-size:11px;line-height:13px;color:#444}
.card .more{margin:16px auto 0;width:106px;height:34px;border:2px solid var(--dark);border-radius:17px;font-size:11px;font-weight:700;display:flex;align-items:center;justify-content:center}

/* team */
.team{left:0;top:1245px;width:1200px;height:766px;background:radial-gradient(ellipse at 50% 25%,#fbfff0 0%,#e4f7b8 45%,var(--lime) 100%)}
.team-notch{left:0;top:1244px}
.frame{top:1483px;width:359px;height:309px;background:var(--dark);border-radius:4px}
.frame-photo{top:1495px;width:397px;height:286px}
.member{width:420px;text-align:center}
.member h4{font-family:"Roboto",sans-serif;font-weight:500;font-size:20px;color:var(--green-text)}
.member .role{margin-top:14px;font-size:14px;color:#222}
.member .mail{margin-top:12px;font-size:13px;font-weight:500;display:flex;gap:8px;justify-content:center;align-items:center}
.member .social{margin:16px auto 0;width:30px;height:30px;border-radius:50%;background:var(--green);font-size:9px;font-weight:700;display:flex;align-items:center;justify-content:center;color:var(--dark)}

/* values */
.values-img{left:0;top:2159px;width:589px;height:407px;border-radius:0 205px 205px 0;background:linear-gradient(120deg,#7a6a55,#c9c3b6 45%,#f0d64a 75%,#e7e3dc)}
.values-title{left:653px;top:2172px;font-size:44px;line-height:54px}
.values-text{left:653px;top:2303px;width:405px;font-size:11px;line-height:15px;color:#333}
.value{top:2391px;width:140px;text-align:center}
.value .ring{margin:0 auto;width:100px;height:100px;border-radius:50%;border:3px solid var(--green);display:flex;align-items:center;justify-content:center}
.value h5{margin-top:12px;font-size:14px;font-weight:500;line-height:16px}
.value p{margin-top:6px;font-size:10px;line-height:12px;color:#444}

/* testimonials */
.testi{left:0;top:2706px;width:1200px;height:575px;background:linear-gradient(120deg,#ebf9d6,#f5fde9 45%,#e1f6b8)}
.quote{left:0;top:2880px;width:1200px;text-align:center;font-size:18px;line-height:23px;color:#222}
.author{left:0;top:2958px;width:1200px;text-align:center}
.author .name{font-size:21px;color:var(--green-text)}
.author .org{font-size:13px;color:#222}
.avatar{border-radius:50%;border:3px solid var(--white)}

/* partners */
.partner{top:3480px;width:136px;height:114px;background:var(--white);box-shadow:0 4px 14px rgba(0,0,0,.12);border-radius:4px;display:flex;align-items:center;justify-content:center;gap:6px;font-size:13px;font-weight:700;color:#555}
.partner i{width:14px;height:14px;background:#cfd4d0;display:block}

/* footer */
.footer{left:0;top:3702px;width:1200px;height:325px;background:var(--green)}
.footer .logo{left:148px;top:3776px;font-size:44px;color:var(--white)}
.fnav{left:417px;top:3785px;display:flex;gap:44px;font-size:14px;font-weight:500;color:var(--dark)}
.fhead{top:3838px;font-family:"Chakra Petch",sans-serif;font-weight:600;font-size:18px;color:var(--white)}
.fitem{top:3870px;display:flex;gap:12px;align-items:center;font-size:11px;line-height:15px;color:var(--white)}
.ficon{width:24px;height:24px;border-radius:50%;background:var(--white);display:flex;align-items:center;justify-content:center;flex:none}
.fsocial{top:3868px;width:32px;height:32px;border-radius:50%;background:var(--white);font-size:9px;font-weight:700;color:var(--dark);display:flex;align-items:center;justify-content:center}
.copy{left:148px;top:3987px;font-size:13px;color:var(--white)}
.legal{left:862px;top:3987px;display:flex;gap:28px;font-size:13px;color:var(--white)}
</style>
</head>
<body>

<!-- header -->
<div class="abs topbar"></div>
<div class="abs logo" style="left:148px;top:14px;font-size:38px;color:var(--green-text)">VEK7</div>
<nav class="abs nav"><span class="active">HOME</span><span>ECOMMERCE</span><span>ONLINE MARKETING</span><span>INTEGRATION</span><span>COMPANY</span></nav>

<!-- hero -->
<section class="abs hero"></section>
<h1 class="abs hero-title">Your online marketing agency<br>in Zurich for SMEs</h1>
<p class="abs hero-sub">You want to reach the right people online and<br>generate more sales. Contact us!</p>
<a class="abs btn btn-offers">OFFERS</a>
<a class="abs btn btn-deadline">DEADLINE</a>
<div class="abs portrait-low"><div class="photo" role="img" aria-label="Portrait of the online marketing manager in a dark suit"></div></div>
<div class="abs portrait-top"><div class="photo" role="img" aria-label="Portrait of the ecommerce manager with arms crossed"></div></div>

<!-- services -->
<h2 class="abs head sec-title" style="top:690px">Our Services</h2>

<article class="abs card" style="left:150px">
  <div class="card-img" role="img" aria-label="Hands using a laptop and phone for online shopping" style="background:linear-gradient(135deg,#2b2b2b,#8a8f96 55%,#d8d4cc)"></div>
  <div class="card-icon"><svg width="24" height="24" viewBox="0 0 24 24"><path d="M2 4h3l3 10h11l2-7H7" fill="none" stroke="#111" stroke-width="2.4"/><circle cx="9" cy="19" r="2" fill="#111"/><circle cx="17" cy="19" r="2" fill="#111"/></svg></div>
  <h3>ECOMMERCE</h3>
  <p>Lorem ipsum dolor sit amet, consectetur Dolor adipiscing elit, sed do eiusmod tempor labore et dolore magna aliqua.</p>
  <div class="more">READ MORE</div>
</article>

<article class="abs card" style="left:458px">
  <div class="card-img" role="img" aria-label="Shopping cart with colourful bags in front of a laptop" style="background:linear-gradient(135deg,#e8e3da,#f2c01c 45%,#3d7be0 75%,#d9d4cb)"></div>
  <div class="card-icon"><svg width="24" height="24" viewBox="0 0 24 24"><rect x="3" y="5" width="18" height="12" rx="1" fill="none" stroke="#111" stroke-width="2"/><path d="M7 14l4-6 4 6z" fill="#111"/><path d="M9 20h6" stroke="#111" stroke-width="2"/></svg></div>
  <h3>ONLINE MARKETING</h3>
  <p>Lorem ipsum dolor sit amet, consectetur Dolor adipiscing elit, sed do eiusmod tempor labore et dolore magna aliqua.</p>
  <div class="more">READ MORE</div>
</article>

<article class="abs card" style="left:767px">
  <div class="card-img" role="img" aria-label="Team joining hands around gear shapes" style="background:radial-gradient(circle at 50% 45%,#d8c48a,#9a8a6a 45%,#3a3f4a)"></div>
  <div class="card-icon"><svg width="24" height="24" viewBox="0 0 24 24"><circle cx="12" cy="12" r="6" fill="none" stroke="#111" stroke-width="4" stroke-dasharray="3 2"/><circle cx="12" cy="12" r="2" fill="#111"/></svg></div>
  <h3>INTEGRATION</h3>
  <p>Lorem ipsum dolor sit amet, consectetur Dolor adipiscing elit, sed do eiusmod tempor labore et dolore magna aliqua.</p>
  <div class="more">READ MORE</div>
</article>

<!-- team -->
<section class="abs team"></section>
<svg class="abs team-notch" width="1200" height="120" viewBox="0 0 1200 120"><path d="M0 0H1200V2L600 112L0 2Z" fill="#fff"/></svg>
<h2 class="abs head sec-title" style="top:1390px">VEK7 Team</h2>

<div class="abs frame" style="left:169px"></div>
<div class="abs frame-photo photo" style="left:181px" role="img" aria-label="Team member portrait against a concrete wall"></div>
<div class="abs frame" style="left:625px"></div>
<div class="abs frame-photo photo" style="left:638px" role="img" aria-label="Team member portrait against a concrete wall"></div>

<div class="abs member" style="left:170px;top:1832px">
  <h4>LUKAS BRENNER</h4>
  <div class="role">Ecommerce Manager</div>
  <div class="mail"><svg width="14" height="10" viewBox="0 0 14 10"><rect width="14" height="10" fill="#111"/><path d="M0 0l7 5 7-5" fill="none" stroke="#fff" stroke-width="1.2"/></svg>lukas@vek7.ch</div>
  <div class="social">Pf</div>
</div>
<div class="abs member" style="left:626px;top:1832px">
  <h4>JONAS KELLER</h4>
  <div class="role">Online Marketing Manager</div>
  <div class="mail"><svg width="14" height="10" viewBox="0 0 14 10"><rect width="14" height="10" fill="#111"/><path d="M0 0l7 5 7-5" fill="none" stroke="#fff" stroke-width="1.2"/></svg>jonas@vek7.ch</div>
  <div class="social">Pf</div>
</div>

<!-- company values -->
<div class="abs values-img" role="img" aria-label="Colleagues working together at a long office table"></div>
<h2 class="abs head values-title">Our Company<br>Values</h2>
<p class="abs values-text">Lorem ipsum dolor sit amet, consectetur adipiscing elit, sed do eiusmod tempor incididunt ut labore et dolore magna aliqua. Ut enim ad minim veniam, quis nostr exercitation ullamco laboris nisi ut aliquip ex ea commodo consequat. Lorem ipsum dolor sit amet, incididunt ut labore et dolore magna aliqua.</p>

<div class="abs value" style="left:646px">
  <div class="ring"><svg width="56" height="56" viewBox="0 0 56 56"><path d="M28 10c-6 4-6 12 0 16 6-4 6-12 0-16z" fill="#111"/><path d="M8 28l10 6 10 4 10-4 10-6v14l-20 8-20-8z" fill="#111"/></svg></div>
  <h5>Sustainability</h5>
  <p>Lorem ipsum dolor sit amet, consectetur adipiscing elit, dolore magna aliqua.</p>
</div>
<div class="abs value" style="left:785px">
  <div class="ring"><svg width="60" height="60" viewBox="0 0 60 60"><circle cx="30" cy="30" r="24" fill="#111"/><circle cx="30" cy="30" r="15" fill="none" stroke="#fff" stroke-width="3"/><path d="M23 30l5 5 9-10" fill="none" stroke="#fff" stroke-width="4"/></svg></div>
  <h5>Quality</h5>
  <p>Lorem ipsum dolor sit amet, consectetur adipiscing elit, dolore magna aliqua.</p>
</div>
<div class="abs value" style="left:921px">
  <div class="ring"><svg width="64" height="50" viewBox="0 0 64 50"><circle cx="32" cy="12" r="8" fill="#111"/><circle cx="14" cy="18" r="6" fill="#111"/><circle cx="50" cy="18" r="6" fill="#111"/><path d="M20 46c0-14 24-14 24 0z" fill="#111"/><path d="M3 44c0-12 20-12 20-2v2zM61 44c0-12-20-12-20-2v2z" fill="#111"/></svg></div>
  <h5>Customer<br>Orientation</h5>
  <p>Lorem ipsum dolor sit amet, dolore magna aliqua.</p>
</div>

<!-- testimonials -->
<section class="abs testi"></section>
<h2 class="abs head sec-title" style="top:2780px;left:-10px">Client Testimonials</h2>
<p class="abs quote">“Thank you for the really successful website<br>solvia.de .It fully meets my expectations. The cooperation was professional and<br>uncomplicated. Again any time.Already have several positivefeedbacks for the get page”.</p>
<div class="abs author"><div class="name">- Marta Lindqvist</div><div class="org">owner of SOLVIA occupational therapy and speech therapy</div></div>

<div class="abs avatar" style="left:238px;top:3071px;width:104px;height:104px;background:linear-gradient(160deg,#d8d4cf,#8a6a58)" role="img" aria-label="Client portrait"></div>
<div class="abs avatar" style="left:325px;top:3065px;width:110px;height:110px;background:linear-gradient(160deg,#e6e6e6,#7e9bc4)" role="img" aria-label="Client portrait"></div>
<div class="abs avatar" style="left:420px;top:3055px;width:122px;height:122px;background:linear-gradient(160deg,#e9e1d6,#d47a68)" role="img" aria-label="Client portrait"></div>
<div class="abs avatar" style="left:660px;top:3057px;width:112px;height:112px;background:linear-gradient(160deg,#e5e5e5,#3d95d8)" role="img" aria-label="Client portrait"></div>
<div class="abs avatar" style="left:775px;top:3063px;width:110px;height:110px;background:linear-gradient(160deg,#4e8a40,#8e3a3a)" role="img" aria-label="Client portrait"></div>
<div class="abs avatar" style="left:866px;top:3068px;width:104px;height:104px;background:linear-gradient(160deg,#ececec,#c4946c)" role="img" aria-label="Client portrait"></div>
<div class="abs avatar" style="left:521px;top:3003px;width:162px;height:162px;border:3px solid var(--green);background:linear-gradient(160deg,#ededed,#b8b2aa 60%,#222)" role="img" aria-label="Portrait of the quoted client"></div>

<!-- partners -->
<h2 class="abs head sec-title" style="top:3366px">Our Partners</h2>
<div class="abs partner" style="left:150px"><i></i>Carta</div>
<div class="abs partner" style="left:303px"><i></i>Wendo</div>
<div class="abs partner" style="left:456px"><i></i>Shelvo</div>
<div class="abs partner" style="left:608px"><i></i>Plimtor Ads</div>
<div class="abs partner" style="left:761px"><i></i>Frendly Ads</div>
<div class="abs partner" style="left:913px"><i></i>Prime Ally</div>

<!-- footer -->
<footer class="abs footer"></footer>
<div class="abs logo" style="left:148px;top:3776px;font-size:44px;color:var(--white)">VEK7</div>
<nav class="abs fnav"><span>HOME</span><span>ECOMMERCE</span><span>ONLINE MARKETING</span><span>INTEGRATION</span><span>COMPANY</span></nav>

<div class="abs fsocial" style="left:150px">Nt</div>
<div class="abs fsocial" style="left:196px">Ch</div>
<div class="abs fsocial" style="left:242px">Pf</div>

<div class="abs fhead" style="left:417px">ADDRESS</div>
<div class="abs fitem" style="left:417px"><span class="ficon"><svg width="12" height="14" viewBox="0 0 12 14"><path d="M6 0a5 5 0 0 1 5 5c0 4-5 9-5 9S1 9 1 5a5 5 0 0 1 5-5z" fill="#111"/><circle cx="6" cy="5" r="2" fill="#fff"/></svg></span>Talweg 14, 8099<br>Zurich, Switzerland</div>

<div class="abs fhead" style="left:667px">CALL US</div>
<div class="abs fitem" style="left:667px"><span class="ficon"><svg width="12" height="12" viewBox="0 0 12 12"><path d="M2 1l2.5 0 1 3-1.5 1a7 7 0 0 0 3 3l1-1.5 3 1V10a1 1 0 0 1-1 1A10 10 0 0 1 1 2a1 1 0 0 1 1-1z" fill="#111"/></svg></span>+41 44 000 27 58</div>

<div class="abs fhead" style="left:892px">EMAIL US</div>
<div class="abs fitem" style="left:892px"><span class="ficon"><svg width="12" height="9" viewBox="0 0 12 9"><rect width="12" height="9" fill="#111"/><path d="M0 0l6 4.5L12 0" fill="none" stroke="#fff"/></svg></span>info@vek7.ch</div>

<div class="abs copy">© 2023 vek7 Marketing GmbH.</div>
<div class="abs legal"><span>Privacy</span><span>Imprint</span><span>AGB</span></div>

</body>
</html>
```